landscape and garden design business card

I would like a business card designed for my landscape and garden design company, Wrenfield Landscapes. We are located in Colorado. I would like to include our logo, contact info, and social media/web site address or QR code. Looking for an organic, flowing design that incorporates our logo.

Target Market(s)

Homeowners and businesses that need garden and landscape design

Contact Information for Business Card

Would like it to say landscape and garden design

Requirements
Must have
• Landscape and garden design

```html
<!DOCTYPE html>
<html lang="en">
<head>
<meta charset="utf-8">
<title>Wrenfield Landscapes – Business Card</title>
<link rel="stylesheet" href="https://fonts.googleapis.com/css2?family=Montserrat:wght@400;500&display=swap">
<style>
  :root {
    --forest: #06231f;
    --cream: #f4eee5;
    --page: #ffffff;
    --page-band: #f1f1f1;
    --sprig: #5f7d70;
  }
  * { margin: 0; padding: 0; box-sizing: border-box; }
  html, body {
    width: 687px;
    height: 1200px;
    overflow: hidden;
    background: var(--page);
    font-family: "Montserrat", sans-serif;
  }
  .stage {
    position: relative;
    width: 687px;
    height: 1200px;
  }
  .stage-band {
    position: absolute;
    inset: 0;
  }
  .card {
    position: absolute;
    left: 63px;
    width: 560px;
    height: 322px;
    box-shadow: 0 12px 30px rgba(0, 0, 0, 0.12);
  }
  .card--front { top: 228px; background: var(--cream); }
  .card--back  { top: 650px; background: var(--forest); }

  .side-band {
    position: absolute;
    left: 48px;
    top: 0;
    width: 67px;
    height: 100%;
    background: var(--forest);
  }
  .side-band__tree {
    position: absolute;
    left: 22px;
    top: 122px;
    width: 23px;
    height: 70px;
    border-radius: 3px;
    background: var(--sprig);
  }

  .brand {
    position: absolute;
    left: 115px;
    right: 0;
    display: flex;
    flex-direction: column;
    align-items: center;
    gap: 12px;
  }
  .card--front .brand { top: 22px; }
  .card--back .brand  { left: 0; top: 56px; gap: 18px; }
  .brand__dot {
    width: 78px;
    height: 78px;
    border-radius: 50%;
    background: var(--forest);
  }
  .card--back .brand__dot { width: 118px; height: 118px; background: var(--cream); }
  .brand__words {
    display: flex;
    flex-direction: column;
    align-items: center;
    gap: 4px;
  }
  .brand__name {
    font-size: 22px;
    font-weight: 500;
    letter-spacing: 0.02em;
    line-height: 28px;
    color: var(--forest);
    white-space: nowrap;
  }
  .brand__tagline {
    font-size: 13px;
    font-weight: 400;
    letter-spacing: 0.06em;
    line-height: 18px;
    color: var(--forest);
    white-space: nowrap;
  }
  .card--back .brand__name { font-size: 27px; line-height: 34px; color: var(--cream); }
  .card--back .brand__tagline { font-size: 15px; line-height: 20px; color: var(--cream); }

  .contact {
    position: absolute;
    left: 171px;
    top: 192px;
    list-style: none;
    color: var(--forest);
    font-size: 17px;
    line-height: 26px;
  }
  .contact__name { font-weight: 500; }
  .contact__line { font-weight: 400; }
</style>
</head>
<body>
<main class="stage">
  <svg class="stage-band" width="687" height="1200" viewBox="0 0 687 1200" aria-hidden="true">
    <polygon points="0,790 687,590 687,960 0,1110" fill="var(--page-band)"/>
  </svg>

  <section class="card card--front" aria-label="Card front">
    <div class="side-band">
      <div class="side-band__tree" role="img" aria-label="Small pine tree illustration"></div>
    </div>
    <div class="brand">
      <span class="brand__dot" aria-hidden="true"></span>
      <div class="brand__words">
        <span class="brand__name">Wrenfield Landscapes</span>
        <span class="brand__tagline">Landscape and garden design</span>
      </div>
    </div>
    <ul class="contact">
      <li class="contact__name">Owen Hartley, Owner</li>
      <li class="contact__line">(303) 555-0187</li>
      <li class="contact__line">contact@wrenfieldlandscapes.com</li>
      <li class="contact__line">www.wrenfieldlandscapes.com</li>
    </ul>
  </section>

  <section class="card card--back" aria-label="Card back">
    <div class="brand">
      <span class="brand__dot" aria-hidden="true"></span>
      <div class="brand__words">
        <span class="brand__name">Wrenfield Landscapes</span>
        <span class="brand__tagline">Landscape and garden design</span>
      </div>
    </div>
  </section>
</main>
</body>
</html>
```